Create Bourbon label for Craft Distillery located in the Foothills of NC.

Need to create a label for a craft bourbon. The brand name is Creekhollow. Looking for a traditional/vintage bottle label. I have created a concept and would like an expansion of the concept idea (open to artwork outside of concept art as well). I have included the bottle being used. Label area approx 4.25H x 3.5W. With the Creekhollow brand name, would like to incorporate trees (native to NC and Appalachia), mountains (mt pano of area included), and sawblade. However, I do not want the sawblade to be the focal point of the design. The word Bourbon, proof, abv, and 750 ml will need to be horizontal. Creekhollow and Made in NC can be angled in the design.

Requirements
Must have
• Front Label will need to contain the followingBrand Name = SawmillsBourbon750 ml100 Proof50% ABVAged 3 years

```html
<!DOCTYPE html>
<html lang="en">
<head>
<meta charset="utf-8">
<title>Creekhollow Bourbon Label</title>
<link rel="stylesheet" href="https://fonts.googleapis.com/css2?family=Rye&family=Arimo:wght@400;700&display=swap">
<style>
  :root {
    --canvas: #ffffff;
    --label-black: #050505;
    --gold: #c9a86a;
    --gold-deep: #8d7242;
    --silver: #d6d6d6;
    --silver-light: #e4e4e4;
    --ink: #1a1a1a;
    --white: #f4f4f4;
  }
  html, body {
    margin: 0;
    padding: 0;
    width: 1200px;
    height: 1040px;
    overflow: hidden;
    background: var(--canvas);
  }
  .canvas {
    position: relative;
    width: 1200px;
    height: 1040px;
  }
  .label {
    position: absolute;
    left: 240px;
    top: 78px;
    width: 720px;
    height: 885px;
  }
  .label-body { fill: var(--label-black); }
  .frame-outer { fill: none; stroke: var(--gold); stroke-width: 3; }
  .frame-inner { fill: none; stroke: var(--gold); stroke-width: 1; }
  .gold-rule { stroke: var(--gold); stroke-width: 3; }
  .ink-rule { stroke: var(--ink); stroke-width: 2; }
  .brand-name {
    font-family: "Rye", serif;
    font-size: 46px;
    fill: var(--white);
  }
  .origin-mark {
    font-family: "Rye", serif;
    font-size: 9px;
    fill: var(--ink);
    letter-spacing: 1px;
  }
  .spirit-name {
    font-family: "Rye", serif;
    font-size: 27px;
    fill: var(--ink);
  }
  .spec-text {
    font-family: "Arimo", sans-serif;
    font-size: 12.5px;
    fill: var(--white);
  }
  .volume-text {
    font-family: "Arimo", sans-serif;
    font-size: 17px;
    fill: var(--white);
  }
  .age-word {
    font-family: "Rye", serif;
    font-size: 6px;
    fill: var(--white);
  }
  .age-number {
    font-family: "Rye", serif;
    font-size: 46px;
    fill: var(--white);
  }
  .age-medallion { fill: url(#medallionShade); stroke: var(--gold); stroke-width: 3; }
  .spec-panel { fill: var(--label-black); stroke: var(--gold); stroke-width: 2; }
</style>
</head>
<body>
<main class="canvas">
  <svg class="label" viewBox="0 0 482 590" xmlns="http://www.w3.org/2000/svg">
    <defs>
      <radialGradient id="sunburstShade" cx="50%" cy="100%" r="80%">
        <stop offset="0%" stop-color="#c9a86a"/>
        <stop offset="60%" stop-color="#5e4c2c"/>
        <stop offset="100%" stop-color="#050505"/>
      </radialGradient>
      <linearGradient id="ridgeShade" x1="0" y1="0" x2="0" y2="1">
        <stop offset="0%" stop-color="#6a6a6a"/>
        <stop offset="100%" stop-color="#d6d6d6"/>
      </linearGradient>
      <radialGradient id="medallionShade" cx="50%" cy="50%" r="50%">
        <stop offset="0%" stop-color="#5a5a5a"/>
        <stop offset="100%" stop-color="#111111"/>
      </radialGradient>
    </defs>

    <path class="label-body" d="M0,75 Q0,58 18,58 L40,58 Q60,58 70,40 Q241,-12 412,40 Q422,58 442,58 L464,58 Q482,58 482,75 L482,515 Q482,532 464,532 L442,532 Q422,532 412,550 Q241,602 70,550 Q60,532 40,532 L18,532 Q0,532 0,515 Z"/>
    <path class="frame-outer" d="M10,82 Q10,68 24,68 L44,68 Q66,68 78,50 Q241,4 404,50 Q416,68 438,68 L458,68 Q472,68 472,82 L472,508 Q472,522 458,522 L438,522 Q416,522 404,540 Q241,588 78,540 Q66,522 44,522 L24,522 Q10,522 10,508 Z"/>
    <path class="frame-inner" d="M17,88 Q17,75 30,75 L48,75 Q70,75 83,58 Q241,14 399,58 Q412,75 434,75 L452,75 Q465,75 465,88 L465,502 Q465,515 452,515 L434,515 Q412,515 399,532 Q241,578 83,532 Q70,515 48,515 L30,515 Q17,515 17,502 Z"/>

    <rect x="26" y="86" width="24" height="24" fill="#c9a86a" opacity="0.55" role="img" aria-label="Corner flourish ornament"/>
    <rect x="432" y="86" width="24" height="24" fill="#c9a86a" opacity="0.55" role="img" aria-label="Corner flourish ornament"/>
    <rect x="26" y="468" width="24" height="24" fill="#c9a86a" opacity="0.55" role="img" aria-label="Corner flourish ornament"/>
    <rect x="432" y="468" width="24" height="24" fill="#c9a86a" opacity="0.55" role="img" aria-label="Corner flourish ornament"/>

    <path d="M110,200 A131,131 0 0 1 372,200 Z" fill="url(#sunburstShade)" role="img" aria-label="Three pine trees before a radiating sunburst"/>

    <line class="gold-rule" x1="98" y1="212" x2="388" y2="190"/>
    <text class="brand-name" x="241" y="262" text-anchor="middle" textLength="390" lengthAdjust="spacingAndGlyphs">CREEKHOLLOW</text>
    <line class="gold-rule" x1="92" y1="292" x2="392" y2="272"/>

    <path d="M186,285 A55,55 0 0 0 296,278 Z" fill="#c9a86a" role="img" aria-label="Circular saw blade"/>
    <text class="origin-mark" x="241" y="310" text-anchor="middle" transform="rotate(-3 241 310)">MADE IN NC</text>

    <rect x="17" y="355" width="448" height="50" fill="url(#ridgeShade)" role="img" aria-label="Panorama of the North Carolina foothill mountains"/>

    <rect x="17" y="405" width="448" height="52" fill="#d6d6d6"/>
    <line class="ink-rule" x1="112" y1="414" x2="162" y2="414"/>
    <line class="ink-rule" x1="122" y1="420" x2="162" y2="420"/>
    <line class="ink-rule" x1="132" y1="426" x2="162" y2="426"/>
    <line class="ink-rule" x1="320" y1="414" x2="370" y2="414"/>
    <line class="ink-rule" x1="320" y1="420" x2="360" y2="420"/>
    <line class="ink-rule" x1="320" y1="426" x2="350" y2="426"/>
    <text class="spirit-name" x="241" y="430" text-anchor="middle" textLength="140" lengthAdjust="spacingAndGlyphs">BOURBON</text>

    <rect class="spec-panel" x="84" y="472" width="314" height="50"/>
    <text class="spec-text" x="96" y="492">100 PROOF</text>
    <text class="spec-text" x="96" y="514">50% ABV</text>
    <text class="volume-text" x="310" y="504">750 ML</text>
    <circle class="age-medallion" cx="241" cy="497" r="42"/>
    <text class="age-word" x="206" y="500" textLength="19" lengthAdjust="spacingAndGlyphs">AGED</text>
    <text class="age-number" x="241" y="515" text-anchor="middle">3</text>
    <text class="age-word" x="256" y="500" textLength="22" lengthAdjust="spacingAndGlyphs">YEARS</text>
  </svg>
</main>
</body>
</html>
```